Fernhill PTA Website Design

We are working with Fernhill Elementary School PTA. They are a Parent Teacher Association that needs a new website design.

A Parent Teacher Association (PTA) is a volunteer organization that brings parents, teachers, and school staff together to support students and enhance their educational experience. PTAs organize fundraisers, sponsor school events, advocate for education policies, and foster stronger connections between families and schools.

Some sites to use for inspiration:

https://gatherpagez.com/demo/
https://nonprofits.kindloopa.com/blogs/more-great-pta-websites-you-should-copy
https://www.qmrvpta.com

Thank you for taking the time to consider designing a website for us. We are web developers based in Stockton and Los Angeles, CA, USA. Most of our projects go through the same process. Understanding this process may help you win a project with us. We custom-code all of our websites in-house. We don’t have any requirements as to what tools you use for your design, but we prefer Figma files. For any design that we label as four-stars, we send it to the client for review. The client picks the final design they want us to use. Once we complete this process, we will continue to show additional clients all the four-star sites and purchase them later. Your designs will have multiple chances to sell. For better chances of success, we ask that you follow these guidelines.

IMAGES:
If you use any images or icons in the design, we ask that you have a link to the asset so we can purchase the image/icon. Most of the designs we submit do not have the customer’s images on them unless they have some great images. Be creative; show us the feeling you are trying to portray with your image choices. Use any royalty-free site you choose. We subscribe to Brisko and mainly use their images, but we can purchase images outside of Brisko.

PLEASE NOTE: we will not submit designs to clients with watermarks on the images.

FONTS:
We ask that you identify the fonts used in the design. This can be done in a message if you want. We typically use Tallowy Fonts and Brisko Fonts.

CONTENT:
We're always open to different content and ideas. We often submit designs with stock images so the client can see our vision. We typically take pictures after the website launch to use their images with our vision. Lorem Ipsum is fine for paragraphs, but we ask that you write the headers in correct English. We want to be able to show the vision and identify the sections of the website.

INSPIRATION:
We typically add a couple of links in the brief of websites we like to help you get started in your design.

REVISIONS:
We do not often ask for revisions of the designs unless we see something in the design that may not appeal to the client. If there are slight changes that we want to make, we do that in the development process.

FEEDBACK:
We rarely give feedback on designs during the design process. We are working on many website projects and do not have the time to provide feedback. We usually respond if your request is well thought out and asks specific questions, but a note asking “feedback, please” usually goes unanswered.

```html
<!DOCTYPE html>
<html lang="en">
<head>
<meta charset="utf-8">
<title>Fernhill PTA</title>
<link href="https://fonts.googleapis.com/css2?family=Russo+One&family=Roboto:wght@400;500;700&display=swap" rel="stylesheet">
<style>
:root{
  --navy:#0c1433;
  --royal:#1f3c80;
  --blue:#213f86;
  --pale:#e4e8f1;
  --grey:#f3f3f6;
  --ink:#1b1b22;
  --text:#33343c;
  --white:#ffffff;
}
*{box-sizing:border-box;margin:0;padding:0}
html,body{width:1200px;height:4008px;overflow:hidden}
body{position:relative;font-family:'Roboto',Arial,sans-serif;color:var(--text);background:var(--white)}
.abs{position:absolute}
.display{font-family:'Russo One','Arial Black',sans-serif;color:var(--ink);text-transform:uppercase;letter-spacing:.5px}
.btn{position:absolute;display:flex;align-items:center;justify-content:center;border-radius:30px;font-weight:700;font-size:15px;text-transform:uppercase;letter-spacing:.2px}
.btn-navy{background:var(--blue);color:var(--white)}
.btn-pale{background:var(--pale);color:var(--blue)}
.underline{position:absolute;height:3px;background:var(--blue)}
.photo{position:absolute}

/* header */
.site-header{position:absolute;left:0;top:0;width:1200px;height:136px;background:var(--navy)}
.brand{position:absolute;left:104px;top:30px;display:flex;align-items:center;gap:10px;color:var(--white);font-weight:700;font-size:16px}
.brand-dot{width:26px;height:26px;border-radius:50%;background:var(--blue);border:2px solid var(--white)}
.nav{position:absolute;top:96px;font-size:16px;font-weight:700;color:var(--white);text-transform:uppercase}
.nav.active{border-bottom:2px solid var(--white);padding-bottom:3px}

/* hero */
.hero-photo{left:0;top:136px;width:1200px;height:556px;background:linear-gradient(100deg,#7f8a63 0%,#b9a98a 18%,#d8dde4 32%,#a85a3c 55%,#9b4b32 75%,#6d8a4c 100%)}
.hero-box{left:269px;top:230px;width:662px;height:277px;background:rgba(255,255,255,.78)}
.hero-title{left:269px;top:255px;width:662px;text-align:center;font-size:37px;line-height:46px}
.hero-text{left:300px;top:356px;width:600px;text-align:center;font-size:19px;line-height:27px;color:#222}
.dot{position:absolute;left:1140px;width:13px;height:13px;border-radius:50%;border:2px solid var(--white)}
.dot.on{background:var(--blue);box-shadow:0 0 0 2px var(--white) inset}

/* about */
.about-text{left:663px;top:900px;width:426px;font-size:15.5px;line-height:26px;text-align:justify;color:#2d2d33}

/* programs */
.programs{left:0;top:1300px;width:1200px;height:708px;background:var(--grey)}
.card{position:absolute;top:1481px;width:302px;height:429px;background:var(--white);border-radius:14px;box-shadow:0 4px 14px rgba(20,30,70,.12)}
.card .pic{position:absolute;left:8px;top:8px;width:286px;height:211px;border-radius:12px}
.card h3{position:absolute;top:242px;width:100%;text-align:center;font-size:18px;font-weight:700;color:var(--ink)}
.card p{position:absolute;top:272px;left:24px;right:24px;text-align:center;font-size:15.5px;line-height:26px}
.card .btn{left:80px;top:365px;width:143px;height:40px}
.circ-arrow{position:absolute;width:33px;height:33px;border-radius:50%}

/* carnival */
.carnival{left:0;top:2008px;width:1200px;height:532px;background:var(--royal)}
.carnival-photo{left:560px;top:2008px;width:640px;height:532px;background:linear-gradient(90deg,var(--royal) 0%,#5f79ad 25%,#a56c3e 55%,#b98556 75%,#c9cfd8 100%)}
.carnival-title{left:110px;top:2078px;font-size:38px;line-height:44px;color:var(--white)}
.carnival-text{left:111px;top:2201px;width:426px;font-size:16.5px;line-height:26px;color:var(--white);text-align:justify}

/* blue & white */
.post-card{left:156px;top:2929px;width:400px;height:211px;background:var(--white);box-shadow:0 6px 16px rgba(20,30,70,.12);border-bottom:3px solid var(--blue)}
.date{position:absolute;height:36px;padding:0 17px;border-radius:20px;background:var(--blue);color:var(--white);font-size:12.5px;font-weight:500;display:flex;align-items:center}
.post-title{position:absolute;font-size:15.5px;font-weight:700;line-height:22px;color:var(--ink);text-transform:uppercase}
.post-text{position:absolute;font-size:13px;line-height:20px;color:#222}
.post-text b{color:var(--blue);text-decoration:underline}

/* contact */
.footer-bg{left:0;top:3436px;width:1200px;height:572px;background:var(--grey)}
.touch{left:44px;top:3244px;width:1112px;height:382px;border-radius:191px;background:var(--navy)}
.field{position:absolute;background:var(--white);border-radius:4px;font-size:14px;color:#222;padding:12px 15px}

/* footer */
.foot-h{position:absolute;top:3700px;font-size:16.5px;font-weight:700;color:var(--ink);text-transform:uppercase}
.foot-list{position:absolute;list-style:none;font-size:14px;color:#222}
.foot-list li{height:39.3px;position:relative;padding-left:31px}
.foot-list li::before{content:"";position:absolute;left:2px;top:6px;width:5px;height:5px;border-radius:50%;background:var(--blue)}
.contact-row{position:absolute;left:565px;display:flex;align-items:center;gap:20px;font-size:14px;line-height:20px;color:#222}
.icon-ring{width:36px;height:36px;border-radius:50%;border:1.5px solid #999;display:flex;align-items:center;justify-content:center;flex:none}
.foot-logo{left:901px;top:3719px;width:186px;height:186px;border-radius:50%;background:var(--blue);display:flex;flex-direction:column;align-items:center;justify-content:center;gap:8px;color:var(--white);font-weight:700;font-size:14px}
.copy{left:0;top:3968px;width:1200px;text-align:center;font-size:12px;color:#333}
</style>
</head>
<body>

<header class="site-header">
  <div class="brand"><span class="brand-dot"></span>FERNHILL PTA</div>
  <div class="btn btn-navy" style="left:783px;top:26px;width:148px;height:44px">Donate Now</div>
  <div class="btn" style="left:940px;top:26px;width:148px;height:44px;background:var(--white);color:var(--blue)">My Account</div>
  <span class="nav active" style="left:328px">Home</span>
  <span class="nav" style="left:407px">Fernhill PTA Store</span>
  <span class="nav" style="left:616px">PTA-Funded Progams</span>
  <span class="nav" style="left:829px">Blue and White</span>
  <span class="nav" style="left:991px">Contact Us</span>
</header>

<section aria-label="Hero">
  <div class="photo hero-photo" role="img" aria-label="Brick elementary school building with trees and front steps"></div>
  <svg class="abs" style="left:0;top:520px" width="1200" height="180" viewBox="0 0 1200 180">
    <polygon points="0,9 156,32 0,118" fill="var(--blue)"/>
    <polygon points="0,118 1200,168 1200,180 0,180" fill="#fff"/>
    <polygon points="0,118 156,32 1200,168" fill="#fff"/>
  </svg>
  <div class="abs hero-box"></div>
  <h1 class="abs display hero-title">Parent Teacher<br>Association</h1>
  <p class="abs hero-text">PTA works hard to provide an incredible array of programs and experiences for all our Fernhill Lions!</p>
  <div class="btn btn-navy" style="left:525px;top:429px;width:150px;height:42px">Get Started</div>
  <span class="dot" style="top:369px"></span>
  <span class="dot on" style="top:395px"></span>
  <span class="dot" style="top:422px"></span>
  <span class="dot" style="top:448px"></span>
</section>

<section aria-label="About">
  <div class="photo" role="img" aria-label="Smiling schoolgirl holding a book in a classroom" style="left:113px;top:727px;width:444px;height:444px;border-radius:50%;background:radial-gradient(circle at 40% 45%,#c7a489 0%,#8f7f8d 45%,#5a6b8a 100%)"></div>
  <div class="abs" style="left:367px;top:946px;width:240px;height:240px;border-radius:50%;background:var(--white);border:9px solid #e6e8ee;display:flex;align-items:center;justify-content:center;gap:8px;font-weight:700;font-size:18px;color:var(--blue)"><span style="width:20px;height:20px;border-radius:50%;background:var(--blue)"></span>FERNHILL PTA</div>
  <h2 class="abs display" style="left:663px;top:762px;font-size:36px;line-height:47px">About<br>Fernhill PTA</h2>
  <div class="underline" style="left:663px;top:858px;width:85px"></div>
  <p class="abs about-text">PTA works hard to provide an incredible array of programs and experiences for all our Fernhill Lions! With an operating budget of approximately $50,000 per year, your support is pivotal to ensuring all our Lions can experience field trips, monthly art lessons, STEM experiments, assemblies, drama program opportunities and more. Please join us by giving back!</p>
  <div class="btn btn-pale" style="left:663px;top:1099px;width:144px;height:43px">Learn More</div>
</section>

<section aria-label="PTA-funded programs">
  <div class="abs programs"></div>
  <h2 class="abs display" style="left:0;top:1390px;width:1200px;text-align:center;font-size:38px">PTA-Funded Programs</h2>
  <div class="underline" style="left:558px;top:1439px;width:85px"></div>

  <svg class="circ-arrow" style="left:40px;top:1680px" viewBox="0 0 33 33"><circle cx="16.5" cy="16.5" r="16.5" fill="#e3e4e8"/><path d="M19 10l-6 6.5 6 6.5" stroke="#222" stroke-width="2.4" fill="none"/></svg>
  <svg class="circ-arrow" style="left:1128px;top:1680px" viewBox="0 0 33 33"><circle cx="16.5" cy="16.5" r="16.5" fill="var(--blue)"/><path d="M14 10l6 6.5-6 6.5" stroke="#fff" stroke-width="2.4" fill="none"/></svg>

  <article class="card" style="left:112px">
    <div class="pic" role="img" aria-label="Children painting at a table with their art teacher" style="background:linear-gradient(135deg,#d9c3a8,#b98e6c 50%,#8f9f8a)"></div>
    <h3>ART PROGRAM</h3>
    <p>Through fundraising and generous donations, our PTA fully funds our entire art program</p>
    <div class="btn btn-pale">Learn More</div>
  </article>
  <article class="card" style="left:448px">
    <div class="pic" role="img" aria-label="Teacher helping a student with classwork" style="background:linear-gradient(135deg,#e7e2d6,#4f7fb8 45%,#c9a47e)"></div>
    <h3>TEACHER SUPPLIES</h3>
    <p>With education budgets being tightened, we like to support our teachers in the big things</p>
    <div class="btn btn-navy">Learn More</div>
  </article>
  <article class="card" style="left:784px">
    <div class="pic" role="img" aria-label="Students exploring nature on a field trip" style="background:linear-gradient(135deg,#8fa56a,#6f8f54 45%,#b59b7a)"></div>
    <h3>FIELD TRIPS</h3>
    <p>Out-of-class experiences are often the ones that really drive home the lessons learned</p>
    <div class="btn btn-pale">Learn More</div>
  </article>
</section>

<section aria-label="Fall carnival">
  <div class="abs carnival"></div>
  <div class="photo carnival-photo" role="img" aria-label="Child in a striped jacket hugging the lion mascot at the carnival"></div>
  <h2 class="abs display carnival-title">2024<br>Fall Carnival</h2>
  <div class="underline" style="left:111px;top:2166px;width:85px;background:var(--white)"></div>
  <p class="abs carnival-text">Join the fun and support the Fernhill 6th Graders! Carnival games, tasty food, yummy treats and loads of fun are just a few weeks away! Bonus: Wear your favorite non-gruesome, non-scary costume and get 2 extra carnival tickets.</p>
  <p class="abs carnival-text" style="top:2341px;text-align:left">** Don't miss out! Pre-purchase Dinner and Carnival Tickets TODAY!**</p>
  <div class="btn" style="left:111px;top:2416px;width:145px;height:45px;background:rgba(255,255,255,.2);color:var(--white)">Learn More</div>
  <svg class="abs" style="left:37px;top:2262px" width="40" height="26" viewBox="0 0 40 26"><path d="M38 13H3M14 2L3 13l11 11" stroke="#fff" stroke-width="2.4" fill="none"/></svg>
  <svg class="abs" style="left:1123px;top:2262px" width="40" height="26" viewBox="0 0 40 26"><path d="M2 13h35M26 2l11 11-11 11" stroke="#fff" stroke-width="2.4" fill="none"/></svg>
</section>

<section aria-label="Blue and White news">
  <h2 class="abs display" style="left:0;top:2640px;width:1200px;text-align:center;font-size:38px">Blue and White</h2>
  <div class="underline" style="left:558px;top:2689px;width:85px"></div>

  <div class="photo" role="img" aria-label="School campus with trees on a sunny day" style="left:112px;top:2733px;width:444px;height:280px;background:linear-gradient(160deg,#dfe6ee,#b8c6d2 35%,#7c9a59 70%,#5b7a3d)"></div>
  <div class="abs post-card">
    <div class="date" style="left:29px;top:-14px">APRIL 27, 2024</div>
    <div class="post-title" style="left:30px;top:36px">It's time to take flight...<br>Jet Set Style!</div>
    <div class="post-text" style="left:30px;top:88px;width:350px">Fernhill's Biennial Blue and White Dinner and Auction is coming up! Peruse the info below... <b>READ MORE</b></div>
  </div>

  <div class="photo" role="img" aria-label="Box of colored pencils and school supplies" style="left:571px;top:2733px;width:251px;height:194px;background:linear-gradient(135deg,#b86a3f,#d9b07b 50%,#a58a6a)"></div>
  <div class="date" style="left:847px;top:2756px">APRIL 27, 2024</div>
  <div class="post-title" style="left:847px;top:2811px">Donate items or dollars</div>
  <div class="post-text" style="left:847px;top:2842px;width:265px">What better way to get involved than to donate a basket for auction! Whether you donate it or you know... <b>READ MORE</b></div>

  <div class="photo" role="img" aria-label="Child packing a blue backpack with books" style="left:571px;top:2943px;width:251px;height:194px;background:linear-gradient(135deg,#c8d2dd,#3a78b5 50%,#8c6a52)"></div>
  <div class="date" style="left:847px;top:2966px">APRIL 27, 2024</div>
  <div class="post-title" style="left:847px;top:3021px">Donate items or dollars</div>
  <div class="post-text" style="left:847px;top:3052px;width:265px">What better way to get involved than to donate a basket for auction! Whether you donate it or you know... <b>READ MORE</b></div>
</section>

<div class="abs footer-bg"></div>

<section aria-label="Get in touch">
  <div class="abs touch"></div>
  <div class="abs" style="left:86px;top:3284px;width:300px;height:300px;border-radius:50%;background:var(--white);display:flex;align-items:center;justify-content:center;gap:10px;font-weight:700;font-size:22px;color:var(--blue)"><span style="width:24px;height:24px;border-radius:50%;background:var(--blue)"></span>FERNHILL PTA</div>
  <h2 class="abs display" style="left:436px;top:3290px;font-size:34px;color:var(--white)">Get in Touch</h2>
  <div class="underline" style="left:436px;top:3337px;width:85px;background:var(--white)"></div>
  <div class="field" style="left:436px;top:3373px;width:211px;height:44px">Your Name</div>
  <div class="field" style="left:655px;top:3373px;width:212px;height:44px">Phone</div>
  <div class="field" style="left:876px;top:3373px;width:212px;height:44px">Email</div>
  <div class="field" style="left:436px;top:3427px;width:652px;height:87px">Your Message</div>
  <div class="btn btn-navy" style="left:675px;top:3529px;width:170px;height:43px">Send Message</div>
</section>

<footer aria-label="Site footer">
  <div class="foot-h" style="left:110px">Navigation</div>
  <ul class="foot-list" style="left:110px;top:3744px">
    <li>Home</li><li>Fernhill PTA Store</li><li>PTA-Funded Progams</li><li>Blue and White</li><li>Contact Us</li>
  </ul>
  <div class="foot-h" style="left:342px">Quick Links</div>
  <ul class="foot-list" style="left:342px;top:3744px">
    <li>FAQ</li><li>Disclaimer</li><li>Privacy Policy</li><li>Terms Of Conditions</li>
  </ul>
  <div class="foot-h" style="left:565px">Contact Us</div>
  <div class="contact-row" style="top:3743px">
    <span class="icon-ring"><svg width="14" height="18" viewBox="0 0 14 18"><path d="M7 17S1 10.5 1 6.5a6 6 0 0112 0C13 10.5 7 17 7 17z" fill="none" stroke="var(--blue)" stroke-width="1.6"/><circle cx="7" cy="6.5" r="2" fill="var(--blue)"/></svg></span>
    <span>1480 Orchard Bend Way Modesto,<br>CA 95350</span>
  </div>
  <div class="contact-row" style="top:3800px">
    <span class="icon-ring"><svg width="16" height="12" viewBox="0 0 16 12"><rect x="0.8" y="0.8" width="14.4" height="10.4" rx="1.5" fill="var(--blue)"/><path d="M1.5 1.5L8 7l6.5-5.5" stroke="#fff" stroke-width="1.3" fill="none"/></svg></span>
    <span>hello@fernhillpta.org</span>
  </div>
  <div class="contact-row" style="top:3854px">
    <span class="icon-ring"><svg width="15" height="15" viewBox="0 0 24 24"><path d="M6.6 10.8a15 15 0 006.6 6.6l2.2-2.2c.3-.3.7-.4 1-.2 1.1.4 2.3.6 3.6.6.6 0 1 .4 1 1V20c0 .6-.4 1-1 1A17 17 0 013 4c0-.6.4-1 1-1h3.5c.6 0 1 .4 1 1 0 1.3.2 2.5.6 3.6.1.3 0 .7-.2 1z" fill="var(--blue)"/></svg></span>
    <span>(209)555-0147</span>
  </div>
  <div class="abs foot-logo"><span style="width:22px;height:22px;border-radius:50%;border:2px solid #fff"></span>FERNHILL PTA</div>
  <div class="abs" style="left:110px;top:3948px;width:978px;height:1px;background:#cfd1d8"></div>
  <div class="abs copy">2025 © ALL RIGHTS RESERVED - FERNHILL PTA</div>
  <div class="abs" style="left:1051px;top:3956px;width:36px;height:36px;border-radius:50%;background:var(--pale)"></div>
</footer>

</body>
</html>
```